Business card for utility of the future

I need a business card template designed for brivolo. We provide sustainable water, energy and waste services to homes.

The card should include name, position, email address, phone number, website and our logo (attached). I would like it to convey professionalism and creativity.

Target Market(s)

Homeowners, investors, corporate partners.

Industry/Entity Type

Utility

Contact Information for Business Card

The card should include name, position, email address, phone number, website and our logo (attached).

```html
<!DOCTYPE html>
<html lang="en">
<head>
<meta charset="utf-8">
<title>brivolo business card</title>
<link href="https://fonts.googleapis.com/css2?family=Open+Sans:wght@400;600;700;800&display=swap" rel="stylesheet">
<style>
  :root {
    --bg: #9a9a9a;
    --bg-dark: #7c7c7c;
    --green: #7ec892;
    --green-text: #78c48c;
    --orange: #ec8f6e;
    --white: #ffffff;
    --ink: #444444;
  }
  * { box-sizing: border-box; margin: 0; padding: 0; }
  html, body {
    width: 1200px; height: 1200px; overflow: hidden;
  }
  body {
    background: radial-gradient(ellipse at 50% 30%, var(--bg) 0%, var(--bg-dark) 100%);
    font-family: "Open Sans", sans-serif;
    position: relative;
  }
  .card {
    position: absolute;
    left: 180px;
    width: 840px;
    height: 480px;
    box-shadow: 0 6px 18px rgba(0,0,0,0.25);
  }
  .card--front { top: 90px; background: var(--green); }
  .card--back { top: 630px; background: var(--white); }

  .wordmark {
    font-weight: 800;
    letter-spacing: -2px;
    line-height: 1;
    white-space: nowrap;
  }

  .card--front .wordmark {
    position: absolute;
    left: 50%; top: 170px;
    transform: translateX(-50%);
    font-size: 104px;
    color: var(--white);
  }
  .social {
    position: absolute;
    left: 50%; top: 378px;
    transform: translateX(-50%);
    display: flex; gap: 22px;
    color: var(--white);
    font-size: 22px;
    white-space: nowrap;
  }
  .social__item { display: flex; align-items: center; gap: 8px; }
  .social__mark {
    width: 22px; height: 22px; border-radius: 50%;
    background: var(--orange);
  }

  .card--back .wordmark {
    position: absolute;
    left: 120px; top: 200px;
    font-size: 88px;
    color: var(--green-text);
  }
  .divider {
    position: absolute;
    left: 468px; top: 150px;
    width: 2px; height: 190px;
    background: var(--orange);
    opacity: 0.7;
  }
  .contact {
    position: absolute;
    left: 500px; top: 150px;
  }
  .contact__name {
    font-size: 30px; font-weight: 600;
    color: var(--green-text);
    line-height: 1.1;
  }
  .contact__role {
    font-size: 22px; color: var(--ink);
    margin-bottom: 12px;
  }
  .contact__list { list-style: none; }
  .contact__list li {
    display: flex; align-items: center; gap: 10px;
    font-size: 20px; color: var(--ink);
    line-height: 1.45;
    white-space: nowrap;
  }
  .contact__icon { width: 18px; height: 18px; flex: none; }
</style>
</head>
<body>

<section class="card card--front">
  <div class="wordmark">brivolo</div>
  <div class="social">
    <span class="social__item"><span class="social__mark"></span>/brivolo</span>
    <span class="social__item"><span class="social__mark"></span>@brivolo</span>
  </div>
</section>

<section class="card card--back">
  <div class="wordmark">brivolo</div>
  <div class="divider"></div>
  <div class="contact">
    <div class="contact__name">Daniel Ostrow</div>
    <div class="contact__role">President</div>
    <ul class="contact__list">
      <li>
        <svg class="contact__icon" viewBox="0 0 18 18"><rect x="1" y="4" width="16" height="11" fill="#ec8f6e"/><path d="M1 4 L9 10 L17 4" fill="none" stroke="#fff" stroke-width="1.5"/></svg>
        info@brivolohome.com
      </li>
      <li>
        <svg class="contact__icon" viewBox="0 0 18 18"><path d="M4 2 L7 2 L8 6 L6 7.5 C7 10 8 11 10.5 12 L12 10 L16 11 L16 14 C16 15 15 16 14 16 C7 15.5 2.5 11 2 4 C2 3 3 2 4 2 Z" fill="#ec8f6e"/></svg>
        (US) 000-0000-0000
      </li>
      <li>
        <svg class="contact__icon" viewBox="0 0 18 18"><path d="M4 2 L7 2 L8 6 L6 7.5 C7 10 8 11 10.5 12 L12 10 L16 11 L16 14 C16 15 15 16 14 16 C7 15.5 2.5 11 2 4 C2 3 3 2 4 2 Z" fill="#ec8f6e"/></svg>
        (ZA) 888-8888-8888
      </li>
      <li>
        <svg class="contact__icon" viewBox="0 0 18 18" fill="none" stroke="#ec8f6e" stroke-width="1.4"><circle cx="9" cy="9" r="7"/><ellipse cx="9" cy="9" rx="3" ry="7"/><path d="M2 9 H16 M3.5 5 H14.5 M3.5 13 H14.5"/></svg>
        www.brivolohome.com
      </li>
    </ul>
  </div>
</section>

</body>
</html>
```